Flyer / Mailer for Business Debt Relief Business - Tillbrook Partners 6" x 11"

We need a 6" x 11" double sided flyer. This will be sent out to potential customers with high interest business loans. We would like the design to coordinate with the colors of our logo. I have included a mock up that we sketched out. I have also included a file of a mailer we received that we would like to use as a template (not colors or fonts, just set up). I have also included an .ai file of our logo.

```html
<!DOCTYPE html>
<html lang="en">
<head>
<meta charset="utf-8">
<title>Tillbrook Partners – Debt Relief Mailer</title>
<link href="https://fonts.googleapis.com/css2?family=Open+Sans:wght@400;600;700&family=Oswald:wght@500;600&family=Roboto+Condensed:wght@700;800&display=swap" rel="stylesheet">
<style>
  :root {
    --green: #7cb82f;
    --green-dark: #5e9a1f;
    --blue: #1f5fae;
    --blue-light: #3a86d4;
    --navy: #0f2f66;
    --charcoal: #3a3a3a;
    --ink: #222;
    --paper: #ffffff;
    --backdrop: #e9e9e9;
  }
  * { box-sizing: border-box; margin: 0; padding: 0; }
  html, body { width: 689px; height: 1200px; overflow: hidden; }
  body { background: var(--backdrop); font-family: "Open Sans", sans-serif; position: relative; }

  .card { position: absolute; left: 34px; width: 620px; height: 338px; background: var(--paper);
          box-shadow: 0 6px 16px rgba(0,0,0,.22); overflow: hidden; }
  .card--front { top: 235px; }
  .card--back { top: 613px; }

  /* ---------- front ---------- */
  .photo { position: absolute; left: 0; width: 166px; }
  .photo--couple { top: 0; height: 87px; background: linear-gradient(135deg, #c9a77f, #e7d3b6 60%, #b98c62); }
  .photo--jar { top: 89px; height: 145px; background: linear-gradient(160deg, #6c87a8, #a7a39a 55%, #7c6a55); }
  .photo--plants { top: 236px; height: 102px; background: linear-gradient(180deg, #eef1ec, #bfd7a8 55%, #8aa56e); }

  .focus-banner { position: absolute; left: 166px; top: 0; width: 356px; height: 88px;
                  background: linear-gradient(160deg, var(--blue-light), var(--blue) 55%, #174a92);
                  text-align: center; padding-top: 18px; color: #fff; }
  .focus-banner__title { font-weight: 700; font-size: 11.5px; color: var(--green); }
  .focus-banner__text { font-size: 11px; line-height: 15px; margin-top: 4px; }

  .brand { position: absolute; display: flex; align-items: center; gap: 5px; color: var(--ink);
           font-family: "Open Sans", sans-serif; font-weight: 600; }
  .brand__mark { width: 12px; height: 12px; background: var(--green); flex: none; }
  .brand--front { left: 522px; top: 0; width: 98px; height: 88px; flex-direction: column;
                  justify-content: center; font-size: 9.5px; text-align: center; line-height: 12px; }
  .brand--front .brand__mark { width: 20px; height: 20px; margin-bottom: 4px; }

  .help-panel { position: absolute; left: 166px; top: 88px; width: 454px; height: 192px;
                background: linear-gradient(100deg, #111 0%, #1d1d1d 30%, #8b97a3 55%, #dfe3e6 75%, #4c5560 100%); }
  .help-panel__text { position: absolute; left: 10px; top: 10px; color: #fff; }
  .help-panel__kicker { font-family: "Roboto Condensed", sans-serif; font-weight: 700; font-size: 10.5px; }
  .help-panel__headline { font-family: "Roboto Condensed", sans-serif; font-weight: 800; font-size: 30px;
                          color: var(--green); line-height: 32px; letter-spacing: .5px; }
  .benefits { list-style: none; margin-top: 6px; }
  .benefits li { display: flex; align-items: center; gap: 6px; font-size: 8px; line-height: 13.5px; }
  .benefits svg { width: 8px; height: 8px; flex: none; }

  .contact-band { position: absolute; left: 166px; top: 280px; width: 454px; height: 58px;
                  background: var(--navy); color: #fff; text-align: center; padding-top: 4px; }
  .contact-band__site { font-size: 11.5px; line-height: 17px; }
  .contact-band__cta { font-size: 11.5px; line-height: 17px; }
  .accent { color: var(--green); font-weight: 700; }
  .contact-line { font-size: 10.5px; line-height: 16px; display: flex; justify-content: center; align-items: center; gap: 4px; }
  .contact-line svg { width: 10px; height: 10px; }

  /* ---------- back ---------- */
  .back-head { position: absolute; left: 0; top: 0; width: 328px; height: 101px;
               background: linear-gradient(135deg, #f4f4f4, #e6e6e6); }
  .brand--back { left: 18px; top: 0; width: 130px; height: 101px; flex-direction: column;
                 justify-content: center; font-size: 13px; text-align: center; }
  .brand--back .brand__mark { width: 28px; height: 28px; margin-bottom: 6px; }
  .back-head__divider { position: absolute; left: 165px; top: 25px; width: 1px; height: 55px; background: #777; }
  .address { position: absolute; left: 172px; top: 36px; width: 150px; text-align: center;
             font-size: 8px; line-height: 11px; color: var(--ink); font-weight: 600; }
  .address svg { width: 18px; height: 18px; display: block; margin: 0 auto 4px; }

  .relief-band { position: absolute; left: 0; top: 101px; width: 342px; height: 85px;
                 background: var(--green);
                 clip-path: polygon(0 0, 342px 0, 342px 78px, 328px 85px, 0 85px);
                 color: #fff; text-align: center; padding: 14px 14px 0 0; }
  .relief-band__title { font-family: "Oswald", sans-serif; font-weight: 600; font-size: 32px; line-height: 36px; }
  .relief-band__sub { font-family: "Open Sans", sans-serif; font-weight: 600; font-size: 15px; line-height: 18px; }

  .pitch { position: absolute; left: 0; top: 186px; width: 328px; height: 69px; background: var(--blue);
           color: #fff; font-size: 13px; line-height: 17px; text-align: center; padding: 8px 10px 0; }
  .back-contact { position: absolute; left: 0; top: 255px; width: 328px; height: 29px;
                  background: linear-gradient(180deg, #4a4a4a, var(--charcoal)); color: #fff;
                  font-size: 11.5px; display: flex; align-items: center; justify-content: center; gap: 4px; }
  .back-contact svg { width: 10px; height: 10px; }
  .stamp-box { position: absolute; left: 538px; top: 20px; width: 64px; height: 63px; border: 1px solid #888; }
</style>
</head>
<body>

<svg width="0" height="0" style="position:absolute">
  <defs>
    <symbol id="icon-phone" viewBox="0 0 24 24"><path fill="#7cb82f" d="M6.6 10.8a15.1 15.1 0 0 0 6.6 6.6l2.2-2.2a1 1 0 0 1 1-.25 11.4 11.4 0 0 0 3.6.57 1 1 0 0 1 1 1V20a1 1 0 0 1-1 1A17 17 0 0 1 3 4a1 1 0 0 1 1-1h3.5a1 1 0 0 1 1 1c0 1.25.2 2.45.57 3.57a1 1 0 0 1-.25 1z"/></symbol>
    <symbol id="icon-mail" viewBox="0 0 24 24"><rect x="2" y="5" width="20" height="14" rx="1" fill="#7cb82f"/><path d="M2 6l10 7 10-7" fill="none" stroke="#fff" stroke-width="1.6"/></symbol>
    <symbol id="icon-tick" viewBox="0 0 10 10"><rect width="10" height="10" rx="2" fill="#7cb82f"/><path d="M2.3 5.2l1.8 1.8 3.6-3.8" fill="none" stroke="#fff" stroke-width="1.5"/></symbol>
  </defs>
</svg>

<!-- Front side -->
<section class="card card--front">
  <div class="photo photo--couple" role="img" aria-label="Photo of a smiling couple saving coins into a piggy bank"></div>
  <div class="photo photo--jar" role="img" aria-label="Photo of a hand dropping a coin into a glass jar beside stacked coins"></div>
  <div class="photo photo--plants" role="img" aria-label="Photo of coin jars with young plants growing from them"></div>

  <div class="focus-banner">
    <p class="focus-banner__title">HELPING BUSINESS FOCUS ON WHAT MATTERS?</p>
    <p class="focus-banner__text">We Understand That Merchant Cash Advance Loans Can Be<br>A Burden On Your Business.</p>
  </div>

  <div class="brand brand--front"><span class="brand__mark"></span>Tillbrook Partners</div>

  <div class="help-panel" role="img" aria-label="Photo of a businesswoman presenting to colleagues in a bright office">
    <div class="help-panel__text">
      <p class="help-panel__kicker">OVERWHELMED BY DAILY/WEEKLY PAYMENTS?</p>
      <p class="help-panel__headline">WE CAN HELP!</p>
      <ul class="benefits">
        <li><svg><use href="#icon-tick"/></svg>This is not a loan, we are not lenders!</li>
        <li><svg><use href="#icon-tick"/></svg>Improve your business cash flow immediately.</li>
        <li><svg><use href="#icon-tick"/></svg>Move payments to one monthly amount.</li>
        <li><svg><use href="#icon-tick"/></svg>Reduce the amount you are paying out monthly.</li>
        <li><svg><use href="#icon-tick"/></svg>Strategic alternatives to high interest loans.</li>
        <li><svg><use href="#icon-tick"/></svg>Fast, confidential business debt relief.</li>
        <li><svg><use href="#icon-tick"/></svg>No-obligation consultation.</li>
        <li><svg><use href="#icon-tick"/></svg>Absolutely no credit pulls.</li>
        <li><svg><use href="#icon-tick"/></svg>No collateral, no financial.</li>
      </ul>
    </div>
  </div>

  <div class="contact-band">
    <p class="contact-band__site">Visit our website: www.<span class="accent">tillbrookrelief</span>.com</p>
    <p class="contact-band__cta"><span class="accent">CALL NOW</span> FOR <span class="accent">FREE</span> CONSULTATION WITH OUR EXPERTS</p>
    <p class="contact-line"><svg><use href="#icon-phone"/></svg>(800) 555-0148 &nbsp;|&nbsp; <svg><use href="#icon-mail"/></svg>info@<span class="accent">tillbrookrelief</span>.com</p>
  </div>
</section>

<!-- Back side -->
<section class="card card--back">
  <div class="back-head">
    <div class="brand brand--back"><span class="brand__mark"></span>Tillbrook Partners</div>
    <span class="back-head__divider"></span>
    <div class="address">
      <svg viewBox="0 0 24 24"><circle cx="12" cy="12" r="11" fill="none" stroke="#7cb82f" stroke-width="2"/><path d="M12 5a4.5 4.5 0 0 0-4.5 4.5C7.5 13 12 18 12 18s4.5-5 4.5-8.5A4.5 4.5 0 0 0 12 5z" fill="#7cb82f"/><circle cx="12" cy="9.5" r="1.6" fill="#fff"/></svg>
      1450 Harmon Ave<br>Millbrook County 75310
    </div>
  </div>

  <div class="relief-band">
    <p class="relief-band__title">STRATEGIC DEBT RELIEF</p>
    <p class="relief-band__sub">FOR BUSINESS OF ALL SIZES</p>
  </div>

  <p class="pitch">Stop taking out loans to pay off other loans. Take back your business's cash flow, and focus on what matters.</p>

  <div class="back-contact"><svg><use href="#icon-phone"/></svg>(800) 555-0148 &nbsp;|&nbsp; <svg><use href="#icon-mail"/></svg>www.<span class="accent">tillbrookrelief</span>.com</div>

  <div class="stamp-box"></div>
</section>

</body>
</html>
```